Brightbay Business Card Design

Our company is called Brightbay. We manufacture confectionary snacks & frozen novelties. Our initial product portfolio includes frozen ice lollies/popsicles & stick ice cream bars.

We require a business card design.

Please use the attached Logo.

Please use an orange, brown, yellow colour code. You may choose any combination of the 3 or include all three. The logo however must remain orange.

Target Market(s)

Business card will be targeted at distributors of our products such as supermarket procurement managers, convenience store owners, wholesale distributors and merchandising agents.

Industry/Entity Type

Business

Requirements
Must have
• Calvin Obeng_Director/ P.O.Box Dunmore 5172, Accra, Ghana / m: 00233(0)507318924/ e: calvin.obeng@mailvora.co.uk

```html
<!DOCTYPE html>
<html lang="en">
<head>
<meta charset="utf-8">
<title>Brightbay Business Card</title>
<link rel="stylesheet" href="https://fonts.googleapis.com/css2?family=Pathway+Gothic+One&display=swap">
<style>
  :root {
    --page: #ffffff;
    --card: #4a1311;
    --card-glow: #5e2219;
    --brand-orange: #f47a20;
    --ink-light: #ffffff;
  }
  * { margin: 0; padding: 0; box-sizing: border-box; }
  html, body {
    width: 1200px;
    height: 900px;
    overflow: hidden;
    background: var(--page);
  }
  .business-card {
    position: absolute;
    left: 74px;
    top: 132px;
    width: 1052px;
    height: 634px;
    background: var(--card);
    overflow: hidden;
    font-family: "Pathway Gothic One", "Arial Narrow", sans-serif;
  }
  .bubble-field {
    position: absolute;
    left: 0;
    top: 0;
    width: 660px;
    height: 634px;
    background: radial-gradient(ellipse at 35% 50%, var(--card-glow) 0%, var(--card) 75%);
  }
  .brand-mark {
    position: absolute;
    left: 80px;
    top: 240px;
    display: flex;
    align-items: center;
    gap: 22px;
    color: var(--brand-orange);
  }
  .brand-dot {
    width: 84px;
    height: 84px;
    border-radius: 50%;
    background: var(--brand-orange);
    flex: none;
  }
  .brand-name {
    font-size: 150px;
    line-height: 1;
    letter-spacing: 1px;
  }
  .contact-block {
    position: absolute;
    right: 44px;
    top: 300px;
    text-align: right;
    color: var(--ink-light);
  }
  .contact-name {
    font-size: 60px;
    line-height: 66px;
    letter-spacing: 1px;
    font-weight: 400;
  }
  .contact-role {
    font-size: 30px;
    line-height: 38px;
    margin-bottom: 2px;
  }
  .contact-line {
    font-size: 31px;
    line-height: 44px;
    letter-spacing: 0.3px;
  }
  .contact-line.city { margin-right: 10px; }
</style>
</head>
<body>
  <main class="business-card">
    <div class="bubble-field" role="img" aria-label="Decorative pattern of overlapping outlined bubbles in muted orange-brown"></div>

    <div class="brand-mark">
      <span class="brand-dot" aria-hidden="true"></span>
      <span class="brand-name">Brightbay</span>
    </div>

    <section class="contact-block">
      <h1 class="contact-name">Calvin Obeng</h1>
      <p class="contact-role">Director</p>
      <p class="contact-line">P.O.Box Dunmore 5172,</p>
      <p class="contact-line city">Accra, Ghana</p>
      <p class="contact-line">m: 00 233 (0) 507 318 924</p>
      <p class="contact-line">e: calvin.obeng@mailvora.co.uk</p>
    </section>
  </main>
</body>
</html>
```